MBRT Needs Fundraiser Dinner Invite!!

The Marita Brenkoll Foundation, a 501 3(c) non for profit has a yearly fundraiser, with varying themes. Last year it was "cowboys" and "cowgirls"
This year, it is Parlor 88, or 70's disco music. I have uploaded last years invite for reference, some stock photography for inspiration. You are not limited to using the stock photos.

Annual MBRT Fundraiser Dinner
October 13th, 2022
Starts: 6:30pm
RSVP By: September 20th
Place: The Oxmere
Price: $135 per ticket

Target Market(s)

Donors, Business People, Every person

Industry/Entity Type

Non for Profit

Font styles to use
Sans Serif

Colors
0054AA
0677BA
7BADD7
CADEEF
E8F1F8
E54698
E96AAD
F1A4CE
F9D9EA
FCEFF6
6B429C
8869AF
B7A5CE
E3DAEB
F3F0F8

Requirements
Must have
• The invite should be 5x7, be sophisticated as the clientele are mainly business people that come to support the cause. It should be fun and inviting at the same time.

```html
<!DOCTYPE html>
<html lang="en">
<head>
<meta charset="utf-8">
<title>MBRT Fundraiser Dinner Invitation</title>
<link rel="stylesheet" href="https://fonts.googleapis.com/css2?family=Bebas+Neue&family=Oswald:wght@400&display=swap">
<style>
  :root {
    --magenta: #D7137A;
    --plum-light: #8C2D6B;
    --plum: #5F2A50;
    --plum-deep: #4A2341;
    --ray: #F6D3E5;
    --guitar-tone: #6E305F;
    --butterfly-tone: #C9538F;
    --white: #FFFFFF;
  }
  html, body {
    margin: 0;
    padding: 0;
    width: 858px;
    height: 1200px;
    overflow: hidden;
    background: var(--magenta);
  }
  .invite {
    display: block;
    width: 858px;
    height: 1200px;
  }
  .bg-base { fill: var(--magenta); }
  .beam-outer { fill: var(--plum-light); }
  .beam-mid { fill: var(--plum); }
  .beam-core { fill: var(--plum-deep); }
  .ray { fill: var(--ray); }
  .guitar-area { fill: var(--guitar-tone); }
  .butterfly-area { fill: var(--butterfly-tone); }
  .brand-name, .eyebrow, .headline, .event-detail, .ticket-text {
    font-family: "Bebas Neue", "Oswald", sans-serif;
  }
  .brand-name { fill: var(--white); font-size: 38px; letter-spacing: 3px; }
  .eyebrow { fill: var(--white); font-size: 32px; }
  .headline { fill: var(--white); }
  .headline--acronym { font-size: 236px; }
  .headline--main { font-size: 214px; }
  .event-detail { fill: var(--white); }
  .event-detail--large { font-size: 76px; }
  .event-detail--small { font-size: 50px; }
  .ticket-box { fill: var(--white); }
  .ticket-text { fill: var(--magenta); }
  .tagline {
    font-family: "Oswald", sans-serif;
    font-weight: 400;
    font-size: 26px;
    fill: var(--white);
  }
</style>
</head>
<body>
<svg class="invite" viewBox="0 0 858 1200" width="858" height="1200" xmlns="http://www.w3.org/2000/svg">
  <!-- Background spotlight beams -->
  <g class="background">
    <rect class="bg-base" x="0" y="0" width="858" height="1200"/>
    <polygon class="beam-outer" points="0,0 858,0 858,90 470,1200 330,1200 0,80"/>
    <polygon class="beam-mid" points="128,0 735,0 450,1200 380,1200"/>
    <polygon class="beam-core" points="250,0 610,0 428,1200 408,1200"/>
  </g>

  <!-- Light streaks -->
  <g class="rays">
    <path class="ray" d="M200,314 L128.8,228.5 L117.2,239.5 Z"/><circle class="ray" cx="123" cy="234" r="8"/>
    <path class="ray" d="M332,377 L273.4,214 L258.6,220 Z"/><circle class="ray" cx="266" cy="217" r="8"/>
    <path class="ray" d="M203,429 L106.7,370 L99.3,384 Z"/><circle class="ray" cx="103" cy="377" r="8"/>
    <path class="ray" d="M649,603 L745.5,659.2 L752.5,644.8 Z"/><circle class="ray" cx="749" cy="652" r="8"/>
    <path class="ray" d="M523,652 L595.2,801.3 L610.8,792.7 Z"/><circle class="ray" cx="603" cy="797" r="9"/>
    <path class="ray" d="M657,712 L731.3,797.7 L742.7,786.3 Z"/><circle class="ray" cx="737" cy="792" r="8"/>
    <path class="ray" d="M269,840 L109.2,905.1 L118.8,924.9 Z"/><circle class="ray" cx="114" cy="915" r="11"/>
    <path class="ray" d="M183,1003 L97.5,1074.2 L108.5,1085.8 Z"/><circle class="ray" cx="103" cy="1080" r="8"/>
    <path class="ray" d="M317,969 L261.8,1059.3 L276.2,1066.7 Z"/><circle class="ray" cx="269" cy="1063" r="8"/>
  </g>

  <!-- Illustration areas -->
  <rect class="guitar-area" role="img" aria-label="Engraved-style illustration of an acoustic guitar in pink" x="305" y="222" width="232" height="670" rx="22"/>
  <rect class="butterfly-area" role="img" aria-label="White sketched butterfly" x="186" y="312" width="100" height="97" rx="12"/>
  <rect class="butterfly-area" role="img" aria-label="White sketched butterfly" x="574" y="617" width="101" height="100" rx="12"/>
  <rect class="butterfly-area" role="img" aria-label="White sketched butterfly" x="200" y="897" width="100" height="98" rx="12"/>

  <!-- Foundation name -->
  <g class="brand">
    <text class="brand-name" x="429" y="128" text-anchor="middle">The Marita Brenkoll</text>
    <text class="brand-name" x="429" y="168" text-anchor="middle">Foundation</text>
  </g>

  <!-- Headline block -->
  <g class="headline-block">
    <text class="eyebrow" x="83" y="503" textLength="432" lengthAdjust="spacingAndGlyphs" transform="rotate(-12.5 83 503)">THE MARITA BRENKOLL FOUNDATION</text>
    <text class="headline headline--acronym" x="526" y="410" textLength="250" lengthAdjust="spacingAndGlyphs" transform="rotate(-12.5 526 410)">MBRT</text>
    <text class="headline headline--main" x="86" y="666" textLength="694" lengthAdjust="spacingAndGlyphs" transform="rotate(-12.5 86 666)">FUNDRAISER</text>
    <text class="headline headline--main" x="86" y="826" textLength="395" lengthAdjust="spacingAndGlyphs" transform="rotate(-12.5 86 826)">DINNER</text>
  </g>

  <!-- Event details -->
  <g class="event-details">
    <text class="event-detail event-detail--large" x="352" y="966" textLength="428" lengthAdjust="spacingAndGlyphs" transform="rotate(-12.5 352 966)">THURSDAY OCT 13TH 2022</text>
    <text class="event-detail event-detail--large" x="352" y="1029" textLength="428" lengthAdjust="spacingAndGlyphs" transform="rotate(-12.5 352 1029)">6:30PM | THE OXMERE</text>
    <text class="event-detail event-detail--small" x="352" y="1077" textLength="428" lengthAdjust="spacingAndGlyphs" transform="rotate(-12.5 352 1077)">RSVP ON OR BEFORE SEP 20TH 2022</text>
  </g>

  <!-- Ticket price -->
  <g class="ticket">
    <polygon class="ticket-box" points="655,1023 772,1000 772,1200 655,1200"/>
    <text class="ticket-text" x="669" y="1069" font-size="40" textLength="86" lengthAdjust="spacingAndGlyphs" transform="rotate(-12.5 669 1069)">TICKETS</text>
    <text class="ticket-text" x="669" y="1122" font-size="72" textLength="88" lengthAdjust="spacingAndGlyphs" transform="rotate(-12.5 669 1122)">$135</text>
    <text class="ticket-text" x="672" y="1150" font-size="24" textLength="85" lengthAdjust="spacingAndGlyphs" transform="rotate(-12.5 672 1150)">PER PERSON</text>
  </g>

  <!-- Tagline -->
  <text class="tagline" x="91" y="1140" textLength="515" lengthAdjust="spacing">EXPERIENCE THE BEST OF THE 70’S</text>
</svg>
</body>
</html>
```